Commercial Property Buying Business - Business Card Design

We need a business card design for a commercial property buying service pitched to mature, sophisticated property investors.
It needs to be simple, elegant, highly professional looking, and simple to read.
I need to be able to change the names and phone numbers on the design.
The old design is attached for guidance of the text required, not necessarily the design.
Hi resolution is very important.
The only graphic is to be the logo.
Less is more

Target Market(s)

55-75 year old mature, experienced, sophisticated male professionals

Industry/Entity Type

Real Estate

Contact Information for Business Card

I have attached MS word with the details of the business cards.
Must have the logo (attached) on front and back.
Must be editable to accommodate use of different names, phone numbers, emails, etc for different individuals within our company

Font styles to use
Serif
Script

Requirements
Must have
• A sophisticated, easy to read layout and font.
• Must have logo
• Text as attached in MS word document.
• The design must be able to be used with elevated print
Nice to have
• Simplicity

```html
<!DOCTYPE html>
<html lang="en">
<head>
<meta charset="utf-8">
<title>Meridian Estates – Business Card</title>
<link rel="stylesheet" href="https://fonts.googleapis.com/css2?family=Alegreya:wght@400;700&display=swap">
<style>
  :root {
    --gold: #e0a431;
    --ink: #0e0e0e;
    --page: #ffffff;
  }
  * { margin: 0; padding: 0; box-sizing: border-box; }
  html, body { width: 1200px; height: 2216px; overflow: hidden; background: var(--page); }
  body {
    font-family: "Alegreya", Georgia, serif;
    display: flex;
    align-items: center;
    justify-content: center;
    gap: 60px;
  }
  .card {
    width: 500px;
    height: 924px;
    position: relative;
    display: flex;
    flex-direction: column;
    box-shadow: 0 2px 10px rgba(0,0,0,0.12);
  }
  .card-front { background: var(--ink); }
  .card-back { background: var(--gold); color: var(--ink); }

  .brand {
    display: flex;
    align-items: center;
    justify-content: center;
    gap: 14px;
    font-weight: 700;
    font-size: 38px;
    letter-spacing: 0.5px;
  }
  .brand-dot {
    width: 26px; height: 26px;
    border-radius: 50%;
    background: currentColor;
  }
  .card-front .brand { color: var(--gold); margin-top: 340px; }
  .card-back .brand { color: var(--ink); margin-top: 96px; }

  .front-band {
    margin-top: auto;
    height: 150px;
    background: var(--gold);
    color: var(--ink);
    display: flex;
    align-items: center;
    justify-content: center;
    text-align: center;
    font-size: 22px;
    line-height: 1.35;
    padding: 0 60px;
  }

  .holder { text-align: center; margin-top: 70px; }
  .holder-name { font-weight: 700; font-size: 40px; font-variant: small-caps; letter-spacing: 1px; }
  .holder-role { font-size: 17px; letter-spacing: 2px; margin-top: 2px; }

  .contact {
    text-align: center;
    font-size: 24px;
    line-height: 1.4;
    font-weight: 700;
    margin: 40px auto 0;
    width: 340px;
    padding-bottom: 22px;
    border-bottom: 2px solid var(--ink);
  }
  .address {
    text-align: center;
    font-size: 24px;
    line-height: 1.4;
    font-weight: 700;
    margin: 26px auto 0;
    width: 340px;
    padding-bottom: 22px;
    border-bottom: 2px solid var(--ink);
  }

  .back-band {
    margin-top: auto;
    height: 150px;
    background: var(--ink);
    color: var(--gold);
    display: flex;
    flex-direction: column;
    align-items: center;
    justify-content: center;
    text-align: center;
  }
  .company { font-weight: 700; font-size: 21px; }
  .company-number { font-size: 15px; margin-top: 4px; letter-spacing: 1px; }
</style>
</head>
<body>
  <section class="card card-front">
    <div class="brand"><span class="brand-dot"></span>Meridian Estates</div>
    <div class="front-band">We buy commercial property from sellers who provide part vendor terms.</div>
  </section>

  <section class="card card-back">
    <div class="brand"><span class="brand-dot"></span>Meridian Estates</div>
    <div class="holder">
      <p class="holder-name">“Dr. Elias Varennes”</p>
      <p class="holder-role">DIRECTOR</p>
    </div>
    <div class="contact">
      <p>T: +61 (0) 3 9000 1234</p>
      <p>M: +61 (0) 400 555 018</p>
      <p>Elias@Meridian.Estates</p>
    </div>
    <div class="address">
      <p>P.O.Box 482</p>
      <p>Harbourton, Victoria 3999</p>
      <p>www.Meridian.Estates</p>
    </div>
    <div class="back-band">
      <p class="company">Meridian Estates Holdings Pty Ltd</p>
      <p class="company-number">ACN 000 111 222</p>
    </div>
  </section>
</body>
</html>
```